Postcard with promo code

We'd like to get a postcard designed to send to our customers with promotional offers. The postcard should have our logo incorporated along with some nice graphics of our products.

The promo card should have the following:
-Placeholder for offering like '$20 Off $50 or more total order'.
-Placeholder for promo code
-Placeholder for time limit.
-Incorporate some graphics of our products (see attached)
-Logo

You can use any number of the graphics attached for the design.

Reference to our website:
Website: www.plumedaisy.com
Email: info@plumedaisy.com
Phone: 374-629-4071

Need to have the design files Illustrator (AI) and Photoshop (PSD) formats.

Industry/Entity Type

Promo

Requirements
Must have
• The promo card should have the following:
• -Placeholder for offering like '$20 Off $50 or more total order'.
• -Placeholder for promo code
• -Placeholder for time limit.
• -Incorporate some graphics of our products (see attached)
• -Logo

```html
<!DOCTYPE html>
<html lang="en">
<head>
<meta charset="utf-8">
<title>Plume Daisy Promo Postcard</title>
<link rel="stylesheet" href="https://fonts.googleapis.com/css2?family=Cinzel:wght@500;700&family=Oswald:wght@500;700&family=Open+Sans:wght@400;600&display=swap">
<style>
:root{
  --stage:#262424;
  --paper:#ffffff;
  --fabric:#e8e5e0;
  --brand-red:#8e1016;
  --deep-red:#7a0d12;
  --cream:#f7ecd0;
  --charcoal:#454343;
  --ink:#2f2626;
  --brand-cream:#e8dcc0;
  --brand-muted:#a59c88;
  --stamp:#8a8a8a;
}
*{box-sizing:border-box;margin:0;padding:0}
html,body{width:900px;height:1200px;overflow:hidden;background:var(--stage)}
.canvas{position:relative;width:900px;height:1200px}
.card{position:absolute;left:97px;width:706px;background:var(--paper);overflow:hidden}
.card--front{top:32px;height:546px;background:var(--fabric)}
.card--back{top:625px;height:545px}
.card-art{position:absolute;inset:0;width:100%;height:100%}
.brand-name{position:absolute;font-family:"Cinzel",serif;font-weight:500;letter-spacing:1px;white-space:nowrap;transform:translateX(-50%)}
.card--front .brand-name{left:578px;top:248px;font-size:27px;color:var(--brand-cream)}
.card--back .brand-name{left:527px;top:62px;font-size:19px;color:var(--brand-muted)}
.offer-box{position:absolute;left:30px;top:430px;width:323px;height:91px;background:var(--paper);border-radius:8px;padding:6px;box-shadow:0 2px 4px rgba(0,0,0,.2)}
.offer-box__inner{width:100%;height:100%;border:2px dashed var(--brand-red);border-radius:6px;display:flex;flex-direction:column;justify-content:center;align-items:center;font-family:"Oswald",sans-serif;font-weight:500;color:var(--brand-red);text-transform:uppercase;line-height:1.15}
.offer-box__title{font-size:22px}
.offer-box__detail{font-size:18px}
.promo-code{position:absolute;left:383px;top:401px;width:296px;height:64px;background:var(--brand-red);border-radius:6px;padding:5px;box-shadow:0 2px 4px rgba(0,0,0,.25)}
.promo-code__inner{width:100%;height:100%;border:2px dashed rgba(255,255,255,.8);border-radius:4px;display:flex;align-items:center;justify-content:center;font-family:"Oswald",sans-serif;font-weight:700;font-size:40px;color:#fff;letter-spacing:.5px}
.time-limit{position:absolute;left:383px;top:494px;width:296px;height:30px;background:var(--paper);display:flex;align-items:center;justify-content:center;font-family:"Open Sans",sans-serif;font-size:16px;color:var(--brand-red);box-shadow:0 2px 3px rgba(0,0,0,.2)}
.stamp-box{position:absolute;left:615px;top:27px;width:61px;height:61px;border:1px solid var(--stamp)}
.contact-band{position:absolute;left:0;top:303px;width:386px;height:104px;background:var(--cream);padding:11px 0 0 36px;list-style:none}
.contact-band li{display:flex;align-items:center;height:30px;font-family:"Cinzel",serif;font-weight:700;font-size:18px;color:var(--ink);letter-spacing:.3px}
.contact-band svg{width:19px;height:19px;margin-right:12px;flex:none}
</style>
</head>
<body>
<div class="canvas">

  <section class="card card--front">
    <svg class="card-art" viewBox="0 0 706 546">
      <defs>
        <linearGradient id="ringPhoto" x1="0" y1="0" x2="1" y2="1">
          <stop offset="0" stop-color="#cfcac3"/>
          <stop offset=".45" stop-color="#a99878"/>
          <stop offset="1" stop-color="#e4e0da"/>
        </linearGradient>
        <radialGradient id="thumbPhoto">
          <stop offset="0" stop-color="#8c6a6a"/>
          <stop offset="1" stop-color="#d9d2cb"/>
        </radialGradient>
      </defs>
      <path role="img" aria-label="Product photo: gold flower ring set with a pearl and small crystals on woven fabric" d="M0,0 H706 V70 C470,230 420,330 300,375 C200,395 90,400 0,402 Z" fill="url(#ringPhoto)"/>
      <path d="M300,375 C420,330 470,230 706,70 V365 C600,380 450,372 300,375 Z" fill="var(--brand-red)"/>
      <path d="M310,370 C430,318 480,212 706,58 V345 C600,352 450,352 310,370 Z" fill="var(--cream)"/>
      <path d="M395,300 C470,250 520,180 706,95 V325 C600,330 490,322 395,300 Z" fill="var(--charcoal)"/>
      <g role="img" aria-label="Product thumbnail: sapphire ring">
        <circle cx="453" cy="181" r="30" fill="#fff" stroke="var(--deep-red)" stroke-width="3"/>
        <circle cx="453" cy="181" r="24" fill="url(#thumbPhoto)"/>
      </g>
      <g role="img" aria-label="Product thumbnail: ruby and emerald ring">
        <circle cx="541" cy="133" r="34" fill="#fff" stroke="var(--deep-red)" stroke-width="3"/>
        <circle cx="541" cy="133" r="28" fill="url(#thumbPhoto)"/>
      </g>
      <g role="img" aria-label="Product thumbnail: emerald marquise ring">
        <circle cx="645" cy="123" r="41" fill="#fff" stroke="var(--deep-red)" stroke-width="3"/>
        <circle cx="645" cy="123" r="34" fill="url(#thumbPhoto)"/>
      </g>
    </svg>
    <div class="brand-name">PLUME DAISY</div>
    <div class="offer-box">
      <div class="offer-box__inner">
        <span class="offer-box__title">Placeholder for offering</span>
        <span class="offer-box__detail">$20 off $50 or more total order</span>
      </div>
    </div>
    <div class="promo-code"><div class="promo-code__inner">PROMO CODE</div></div>
    <div class="time-limit">Placeholder For Time Limit.</div>
  </section>

  <section class="card card--back">
    <svg class="card-art" viewBox="0 0 706 545">
      <defs>
        <linearGradient id="setPhoto" x1="0" y1="0" x2="1" y2="1">
          <stop offset="0" stop-color="#e6e3de"/>
          <stop offset=".4" stop-color="#5c5a66"/>
          <stop offset=".7" stop-color="#cfcbc5"/>
          <stop offset="1" stop-color="#e9e6e2"/>
        </linearGradient>
      </defs>
      <rect role="img" aria-label="Product photo: sapphire earrings, pendant and ring set on white fabric" x="0" y="0" width="420" height="545" fill="url(#setPhoto)"/>
      <path d="M345,0 H706 V545 H227 C240,500 265,450 305,400 C400,270 410,120 345,0 Z" fill="var(--paper)"/>
      <path d="M368,0 H396 C452,90 448,185 408,250 C428,165 418,80 368,0 Z" fill="var(--charcoal)"/>
      <path d="M330,0 H360 C440,110 430,260 320,410 C272,470 242,510 234,545 H222 C233,500 258,450 298,400 C392,275 402,120 330,0 Z" fill="var(--brand-red)"/>
    </svg>
    <div class="brand-name">PLUME DAISY</div>
    <div class="stamp-box"></div>
    <ul class="contact-band">
      <li>
        <svg viewBox="0 0 20 20" fill="none" stroke="var(--brand-red)" stroke-width="1.6"><circle cx="10" cy="10" r="8"/><ellipse cx="10" cy="10" rx="3.5" ry="8"/><path d="M2 10h16M3.5 6h13M3.5 14h13"/></svg>
        www.plumedaisy.com
      </li>
      <li>
        <svg viewBox="0 0 20 20" fill="none" stroke="var(--brand-red)" stroke-width="1.6"><rect x="2" y="4.5" width="16" height="11"/><path d="M2 4.5l8 6.5 8-6.5"/></svg>
        info@plumedaisy.com
      </li>
      <li>
        <svg viewBox="0 0 20 20" fill="none" stroke="var(--brand-red)" stroke-width="1.6"><circle cx="10" cy="10" r="8.5"/><path d="M7 5.5l1.6 2.4-1 1.2c.6 1.3 1.6 2.3 2.9 2.9l1.2-1 2.4 1.6-.9 1.6c-3.5-.3-6.5-3.3-6.8-6.8z"/></svg>
        374-629-4071
      </li>
    </ul>
  </section>

</div>
</body>
</html>
```